Business Card Design Project

Tarvolink - based in Melbourne, Australia. We plan, design, implement and support network infrastructure (Plemba, Hollvask, Kestrix, Stormpike etc).

Target Market(s)

Small/Medium enterprise and Corporate.

Industry/Entity Type

Business

```html
<!DOCTYPE html>
<html lang="en">
<head>
<meta charset="utf-8">
<title>Tarvolink Business Card</title>
<link href="https://fonts.googleapis.com/css2?family=Open+Sans:wght@400;600;700&display=swap" rel="stylesheet">
<style>
  :root {
    --orange: #e07f12;
    --orange-light: #ee9a3c;
    --grey: #6b6c6e;
    --grey-dark: #58595b;
    --grey-soft: #7a7b7d;
    --white: #ffffff;
    --text: #4a4a4c;
    --backdrop: #e4e4e4;
  }
  * { margin: 0; padding: 0; box-sizing: border-box; }
  html, body { width: 1200px; height: 725px; overflow: hidden; }
  body {
    background: var(--backdrop);
    font-family: "Open Sans", Arial, sans-serif;
    position: relative;
  }
  .card {
    position: absolute;
    top: 214px;
    width: 520px;
    height: 297px;
    overflow: hidden;
    box-shadow: 0 6px 18px rgba(0,0,0,0.18);
  }

  /* ---------- Front ---------- */
  .card-front { left: 50px; background: var(--white); }
  .front-top-band {
    position: absolute; left: 0; top: 0; width: 100%; height: 20px;
    background: var(--orange);
  }
  .front-top-band::after {
    content: ""; position: absolute; left: 0; top: 0; width: 100%; height: 100%;
    background: linear-gradient(100deg, transparent 62%, var(--orange-light) 62%, var(--orange-light) 78%, transparent 78%);
  }
  .front-bottom-band {
    position: absolute; left: 0; bottom: 0; width: 100%; height: 44px;
  }
  .person { position: absolute; left: 26px; top: 40px; }
  .person-name {
    font-size: 20px; font-weight: 700; color: var(--orange); line-height: 1.1;
  }
  .person-role {
    font-size: 15px; font-weight: 700; color: var(--orange);
    padding-bottom: 3px; border-bottom: 2px solid var(--grey-soft);
    width: 150px; line-height: 1.3;
  }
  .contact-list { position: absolute; left: 22px; top: 112px; list-style: none; }
  .contact-item {
    display: flex; align-items: center; gap: 12px;
    height: 34px; font-size: 15px; color: var(--text);
  }
  .contact-icon { width: 28px; height: 28px; flex: none; }
  .brand-front {
    position: absolute; left: 300px; top: 96px;
    display: flex; align-items: center; gap: 8px;
  }
  .brand-dot { width: 26px; height: 26px; border-radius: 50%; background: var(--grey); }
  .brand-name-front { font-size: 30px; font-weight: 600; color: var(--orange); letter-spacing: -0.5px; }
  .front-emblem {
    position: absolute; left: 330px; top: 165px;
    width: 180px; height: 180px; border-radius: 50%; background: var(--grey);
  }

  /* ---------- Back ---------- */
  .card-back { left: 630px; background: var(--grey); }
  .back-emblem {
    position: absolute; right: -60px; top: -40px;
    width: 260px; height: 260px; border-radius: 50%; background: var(--grey-soft); opacity: 0.35;
  }
  .brand-back {
    position: absolute; left: 40px; top: 62px;
    display: flex; align-items: center; gap: 12px;
  }
  .brand-back .brand-dot { width: 40px; height: 40px; background: var(--white); }
  .brand-name-back { font-size: 50px; font-weight: 600; color: var(--white); letter-spacing: -1px; line-height: 1; }
  .tagline {
    position: absolute; left: 24px; right: 24px; top: 140px;
    font-size: 11.5px; font-weight: 700; color: var(--white); line-height: 1.45; text-align: center;
  }
  .back-bottom-band {
    position: absolute; left: 0; bottom: 0; width: 100%; height: 42px;
    background: linear-gradient(100deg, var(--orange) 55%, var(--orange-light) 55%, var(--orange-light) 70%, var(--orange) 70%);
  }
</style>
</head>
<body>

<section class="card card-front">
  <div class="front-top-band"></div>
  <svg class="front-bottom-band" viewBox="0 0 520 44" preserveAspectRatio="none">
    <rect x="0" y="0" width="340" height="44" fill="var(--orange)"/>
    <polygon points="0,44 0,20 180,44" fill="var(--orange-light)"/>
    <rect x="340" y="0" width="180" height="44" fill="var(--grey)"/>
  </svg>

  <div class="person">
    <p class="person-name">Tobin Aldcroft</p>
    <p class="person-role">Director</p>
  </div>

  <ul class="contact-list">
    <li class="contact-item">
      <svg class="contact-icon" viewBox="0 0 28 28">
        <circle cx="14" cy="14" r="12.5" fill="none" stroke="var(--orange)" stroke-width="2"/>
        <circle cx="14" cy="14" r="10" fill="var(--grey)"/>
        <path d="M10 9.5c.6-.6 1.3-.6 1.8 0l1 1.3c.4.5.3 1-.1 1.4l-.6.6c.6 1.3 1.5 2.2 2.8 2.8l.6-.6c.4-.4.9-.5 1.4-.1l1.3 1c.6.5.6 1.2 0 1.8l-.8.8c-3.6.2-7.9-4.1-7.7-7.7z" fill="var(--white)"/>
      </svg>
      <span>5550 1928</span>
    </li>
    <li class="contact-item">
      <svg class="contact-icon" viewBox="0 0 28 28">
        <circle cx="14" cy="14" r="12.5" fill="none" stroke="var(--orange)" stroke-width="2"/>
        <circle cx="14" cy="14" r="10" fill="var(--grey)"/>
        <rect x="8.5" y="10" width="11" height="8" fill="var(--white)"/>
        <path d="M8.5 10l5.5 4.5 5.5-4.5" fill="none" stroke="var(--grey)" stroke-width="1"/>
      </svg>
      <span>info@tarvolink.com</span>
    </li>
    <li class="contact-item">
      <svg class="contact-icon" viewBox="0 0 28 28">
        <circle cx="14" cy="14" r="12.5" fill="none" stroke="var(--orange)" stroke-width="2"/>
        <circle cx="14" cy="14" r="10" fill="var(--grey)"/>
        <g fill="none" stroke="var(--white)" stroke-width="1">
          <circle cx="14" cy="14" r="6"/>
          <ellipse cx="14" cy="14" rx="2.6" ry="6"/>
          <line x1="8" y1="14" x2="20" y2="14"/>
          <line x1="9" y1="11" x2="19" y2="11"/>
          <line x1="9" y1="17" x2="19" y2="17"/>
        </g>
      </svg>
      <span>www.tarvolink.com</span>
    </li>
  </ul>

  <div class="brand-front">
    <span class="brand-dot"></span>
    <span class="brand-name-front">tarvolink</span>
  </div>

  <div class="front-emblem" role="img" aria-label="Large decorative brand emblem"></div>
</section>

<section class="card card-back">
  <div class="back-emblem" role="img" aria-label="Faint decorative brand emblem"></div>
  <div class="brand-back">
    <span class="brand-dot"></span>
    <span class="brand-name-back">tarvolink</span>
  </div>
  <p class="tagline">We plan, design, implement and support network infrastructure<br>(Plemba, Hollvask, Kestrix, Stormpike etc).</p>
  <div class="back-bottom-band"></div>
</section>

</body>
</html>
```